Redwell - Rebranding, Namecard, Stationary and One Page Web

Refresh logo, make it modern and design matching name card, stationary and one page web

Redwell Information Technology (Int'l) Company Limited
紅井訊息科技(國際)有限公司

Company is System Integrator, and will be providing products and services to government and enterprise organizations. Our Chief Security Officer came from top U.S. vendor, and had been working on top enterprise and government projects globally, so we want the refreshed image of the new company to have a East Cost U.S. style, with hint of technology from Silicon Valley. The company will also be representing top brands from the U.S. on information security.

Branding refresh is needed because company is being acquired and is expanding

Target Market(s)

Cyber Security

Industry/Entity Type

Information Technology

Contact Information for Business Card

Need Chinese and English

Number of Pages Required

1 page

Font styles to use
Sans Serif

Colors
0292cd
00a990

Requirements
Must have
• Modern, clean, cyber look. Must keep same colors and general look and feel of original logo. Only modernization, do not change its personality

```html
<!DOCTYPE html>
<html lang="en">
<head>
<meta charset="utf-8">
<title>Redwell Name Card</title>
<link href="https://fonts.googleapis.com/css2?family=Arimo:wght@400;700&family=Roboto+Condensed:wght@700&family=Courier+Prime&family=Noto+Serif+TC:wght@300&family=Questrial&display=swap" rel="stylesheet">
<style>
  :root {
    --backdrop-top: #ffffff;
    --backdrop-bottom: #b3b3b3;
    --card-dark: #05090c;
    --card-mid: #0b171b;
    --text-light: #ffffff;
    --text-soft: #e9eef0;
    --brand-blue: #2f86c8;
    --brand-green: #5fb46a;
    --band-white: #ffffff;
    --band-ink: #222222;
  }
  * { margin: 0; padding: 0; box-sizing: border-box; }
  html, body { width: 1200px; height: 1200px; overflow: hidden; }
  body {
    position: relative;
    background: linear-gradient(180deg, var(--backdrop-top) 0%, var(--backdrop-bottom) 100%);
    font-family: "Arimo", Arial, sans-serif;
  }
  .card {
    position: absolute;
    left: 242px;
    width: 756px;
    height: 473px;
    overflow: hidden;
  }
  .card--front { top: 95px; }
  .card--back { top: 650px; }
  .card__texture {
    position: absolute;
    inset: 0;
    background: radial-gradient(ellipse at 70% 40%, var(--card-mid) 0%, var(--card-dark) 70%);
  }
  .card--front .card__texture { bottom: 26px; }

  .brand {
    position: absolute;
    display: flex;
    align-items: center;
    gap: 10px;
    color: var(--brand-blue);
    font-family: "Arimo", Arial, sans-serif;
    font-weight: 700;
  }
  .brand__dot {
    border-radius: 50%;
    background: var(--brand-green);
  }
  .brand--small { left: 24px; top: 34px; font-size: 42px; line-height: 50px; }
  .brand--small .brand__dot { width: 20px; height: 20px; }
  .brand--large { left: 0; right: 0; top: 180px; justify-content: center; font-size: 96px; gap: 20px; }
  .brand--large .brand__dot { width: 44px; height: 44px; }

  .company {
    position: absolute;
    left: 292px;
    top: 22px;
    width: 432px;
    color: var(--text-soft);
  }
  .company__zh {
    font-family: "Noto Serif TC", serif;
    font-weight: 300;
    font-size: 48px;
    line-height: 66px;
    white-space: nowrap;
    transform: scaleX(0.643);
    transform-origin: left center;
  }
  .company__en {
    font-family: "Courier Prime", monospace;
    font-size: 13px;
    line-height: 18px;
    margin-top: 0;
    white-space: nowrap;
  }

  .person {
    position: absolute;
    left: 41px;
    top: 170px;
    color: var(--text-light);
  }
  .person__name {
    font-family: "Roboto Condensed", sans-serif;
    font-weight: 700;
    font-size: 48px;
    line-height: 50px;
  }
  .person__title {
    font-family: "Arimo", Arial, sans-serif;
    font-weight: 400;
    font-size: 19px;
    margin-left: 6px;
  }
  .person__email {
    font-size: 18px;
    line-height: 22px;
    margin-left: 10px;
  }

  .contact {
    position: absolute;
    left: 36px;
    top: 322px;
    color: var(--text-light);
    font-size: 22px;
    line-height: 26px;
  }
  .contact__mobile { margin-top: 26px; }

  .web-band {
    position: absolute;
    left: 0; right: 0; bottom: 0;
    height: 26px;
    background: var(--band-white);
    color: var(--band-ink);
    font-family: "Questrial", sans-serif;
    font-size: 28px;
    letter-spacing: 5px;
    line-height: 30px;
    text-align: center;
  }
</style>
</head>
<body>
  <section class="card card--front">
    <div class="card__texture" role="img" aria-label="Dark circuit board texture"></div>
    <div class="brand brand--small"><span class="brand__dot"></span><span>Redwell</span></div>
    <div class="company">
      <p class="company__zh">紅井訊息科技（國際）有限公司</p>
      <p class="company__en">Redwell Information Technology (Int'l) Company Limited</p>
    </div>
    <div class="person">
      <p class="person__name">Daniel Lau<span class="person__title">CEO</span></p>
      <p class="person__email">daniellau@hkredwell.com.hk</p>
    </div>
    <div class="contact">
      <p>Office: Room B, Unit 418, 4/F, Tak Fung Ind. Bldg,</p>
      <p>No. 12 Sheung Yee Road, Kowloon Bay, Kowloon, HKSAR</p>
      <p class="contact__mobile">Mobile: (852) 5550 1234</p>
    </div>
    <div class="web-band">www.hkredwell.com.hk</div>
  </section>

  <section class="card card--back">
    <div class="card__texture" role="img" aria-label="Dark circuit board texture"></div>
    <div class="brand brand--large"><span class="brand__dot"></span><span>Redwell</span></div>
  </section>
</body>
</html>
```